1 pager agency advertisement flyer

We need a fresh logo and advertising flyer for my insurance company based in Richmond VA. We have recently signed an agreement with a sizable company to become their preferred insurance provider. We specialize in Several things but focusing on Auto, Home, Renters, Roadside assistance, Landlord, Motorcycles, Boats, and Condos. We also offer a full portfolio of financial services. I would like to see options with Blue, yellow and white, and also black(I know), Yellow, and white. The name of the agency is Talvor Insurance Services Inc. Discounts are key in what we do: Discounts to advertise: Multi policy, 19% early signing, safe driver rewards, and EASY PAYMENT OPTIONS. A phrase like: "as an employee you are eligible for a 19% signing discount" SIDE NOTE: The people that we have already written business for the average saving currently stands at 28% annually.

Industry/Entity Type

Graphic Design

```html
<!DOCTYPE html>
<html lang="en">
<head>
<meta charset="utf-8">
<title>Talvor Insurance Services Inc. – Flyer</title>
<link rel="stylesheet" href="https://fonts.googleapis.com/css2?family=Bebas+Neue&family=Libre+Baskerville:wght@700&display=swap">
<style>
  :root{
    --blue:#1d5a8c;
    --blue-dark:#174a75;
    --yellow:#f2d21a;
    --yellow-soft:#f6df52;
    --ink:#121417;
    --paper:#f7f7f7;
    --stage:#d9d9d9;
  }
  *{margin:0;padding:0;box-sizing:border-box}
  html,body{width:898px;height:1200px;overflow:hidden;background:var(--stage)}
  .flyer{
    position:absolute;left:31px;top:11px;width:836px;height:1178px;
    background:var(--paper);overflow:hidden;
  }
  .hero-photo{
    position:absolute;left:0;top:0;width:836px;height:500px;
    background:linear-gradient(160deg,#e9d9b6 0%,#d6b98a 35%,#b9a07a 60%,#e7dcc8 100%);
  }
  .backdrop-photo{
    position:absolute;left:0;top:520px;width:836px;height:540px;
    background:linear-gradient(180deg,#f4f4f4 0%,#e7e7e7 45%,#f2f2f2 100%);
  }
  .waves{position:absolute;left:0;top:0;width:836px;height:1178px}
  .brand-tag{
    position:absolute;left:432px;top:27px;width:402px;height:63px;
    background:var(--blue);color:#fff;
    font-family:"Bebas Neue",sans-serif;font-size:36px;letter-spacing:.5px;
    display:flex;align-items:center;justify-content:center;
  }
  .cover-circle{
    position:absolute;border-radius:50%;border:9px solid var(--yellow);
    box-shadow:0 3px 8px rgba(0,0,0,.3);
  }
  .cover-circle.tow{left:140px;top:384px;width:176px;height:176px;
    background:linear-gradient(160deg,#6f8a5a 0%,#b9b3a6 45%,#c9423a 70%,#6d6d6d 100%)}
  .cover-circle.motorcycle{left:293px;top:344px;width:250px;height:250px;z-index:2;
    background:linear-gradient(170deg,#4f7a3a 0%,#6e9150 40%,#c23428 62%,#5b5f5c 100%)}
  .cover-circle.boat{left:533px;top:378px;width:182px;height:182px;
    background:linear-gradient(160deg,#4aa3d8 0%,#7cc3e0 40%,#3e7a4e 60%,#e2cf9e 100%)}
  .headline{
    position:absolute;left:0;width:836px;text-align:center;white-space:nowrap;
    font-family:"Bebas Neue",sans-serif;color:var(--ink);
  }
  .discounts{top:640px;font-size:33px;line-height:44px}
  .discounts .big{color:var(--blue);font-size:50px;vertical-align:-3px}
  .payment{top:692px;font-size:41px;color:var(--blue);line-height:48px}
  .rule{position:absolute;left:231px;width:385px;height:7px;background:var(--blue);border-radius:3px;z-index:2}
  .rule.top{top:757px}
  .rule.bottom{top:876px}
  .employee-offer{
    position:absolute;left:101px;top:761px;width:631px;height:120px;border-radius:12px;
    background:linear-gradient(180deg,var(--yellow-soft),var(--yellow));
    display:flex;align-items:center;justify-content:center;text-align:center;
    font-family:"Libre Baskerville",serif;font-weight:700;font-size:24px;line-height:33px;color:var(--ink);
  }
  .savings{top:930px;font-size:32px;line-height:40px}
  .savings .big{color:var(--blue);font-size:42px;vertical-align:-2px}
  .contact{position:absolute;left:0;width:836px;text-align:center}
  .phone{top:1080px;font-family:"Bebas Neue",sans-serif;font-size:42px;color:var(--ink);
    display:flex;align-items:center;justify-content:center;gap:10px}
  .phone-icon{width:32px;height:32px}
  .web{top:1123px;font-family:"Libre Baskerville",serif;font-weight:700;font-size:26px;color:var(--ink)}
</style>
</head>
<body>
<div class="flyer">
  <div class="hero-photo" role="img" aria-label="Warm living room interior with sofa, fireplace, TV and coffee table"></div>
  <div class="backdrop-photo" role="img" aria-label="Faded light grey living room interior"></div>

  <svg class="waves" viewBox="0 0 836 1178" aria-hidden="true">
    <path d="M0 420 Q420 600 836 410 L836 1178 L0 1178 Z" fill="var(--yellow)"/>
    <path d="M0 448 Q420 625 836 440 L836 1178 L0 1178 Z" fill="var(--blue)"/>
    <path d="M0 500 Q420 660 836 490 L836 1178 L0 1178 Z" fill="var(--ink)"/>
    <path d="M0 508 Q420 668 836 498 L836 1178 L0 1178 Z" fill="var(--paper)" fill-opacity=".9"/>
    <path d="M0 1038 Q420 1000 836 1026 L836 1178 L0 1178 Z" fill="var(--ink)"/>
    <path d="M0 1046 Q420 1008 836 1034 L836 1178 L0 1178 Z" fill="var(--blue)"/>
    <path d="M0 1080 Q420 1050 836 1064 L836 1178 L0 1178 Z" fill="var(--yellow)"/>
  </svg>

  <div class="brand-tag">Talvor Insurance Services Inc.</div>

  <div class="cover-circle tow" role="img" aria-label="Tow truck for roadside assistance"></div>
  <div class="cover-circle motorcycle" role="img" aria-label="Rider on a red sport motorcycle"></div>
  <div class="cover-circle boat" role="img" aria-label="Wooden boat on a tropical beach"></div>

  <p class="headline discounts">Multi policy, <span class="big">19%</span> early signing, safe driver rewards, and</p>
  <p class="headline payment">Easy payment options.</p>

  <div class="rule top"></div>
  <div class="employee-offer"><p>as an employee you are eligible for a<br>19% signing discount</p></div>
  <div class="rule bottom"></div>

  <p class="headline savings">The people that we have already written business for the<br>average saving currently stands at <span class="big">28%</span> annually.</p>

  <div class="contact phone">
    <svg class="phone-icon" viewBox="0 0 32 32" aria-hidden="true">
      <rect width="32" height="32" rx="6" fill="var(--blue)"/>
      <path d="M11 7c1 0 2 2.5 2.5 4 .3 1-1.5 1.8-1.3 2.8.6 2.5 2.6 4.6 5 5.3 1 .3 1.8-1.5 2.8-1.2 1.5.5 4 1.5 4 2.5 0 2-2 4-4 4C13 24.4 7.6 19 7.6 11c0-2 1.4-4 3.4-4z" fill="var(--yellow)"/>
    </svg>
    <span>555-014-2783</span>
  </div>
  <p class="contact web">www.talvorins.com</p>
</div>
</body>
</html>
```